retail package design for food snack

We need a full package design (front and back)for our retail food snack. It will be printed on a stand up zipper pouch. The snack is crunchy chilli. The the package will need to involve the logo, maybe a picture on the snack etc. we will require the back of the package including nutritional information, ingredients, company details, bar code and a QR code.
We have six flavours, so we would need to change the background colour and also the flavour name on the front (maybe in a circle) I've attached some photos of the product, the logo and what the package currently looks like. Its going to be printed on a stand-up pouch with a zipper lock (I've attached two package examples for reference only not design examples)

• I envision the logo to be large on the package but happy to see all options

```html
<!DOCTYPE html>
<html lang="en">
<head>
<meta charset="utf-8">
<title>Ruby Crunch – Crunchy Chilli Pouch Dieline</title>
<link rel="stylesheet" href="https://fonts.googleapis.com/css2?family=Poppins:wght@400;500;600;700&family=Pathway+Gothic+One&display=swap">
<style>
  :root{
    --ink:#0a0a0a;
    --paper:#ffffff;
    --window:#676767;
    --dim:#e0201b;
    --brand-red:#8e1a16;
    --chilli:#c8201f;
    --hot:#e8581c;
    --tomyum:#1fa64a;
    --pizza:#f5ad1c;
    --bbq:#9b9a96;
  }
  html,body{margin:0;padding:0;background:var(--paper);overflow:hidden}
  .sheet{width:1080px;height:1200px;display:block}
  .dim-text{font-family:"Pathway Gothic One",sans-serif;fill:var(--dim)}
  .dim-line{stroke:var(--dim);stroke-width:1.6;fill:none}
  .guide{stroke:var(--dim);stroke-width:1.2;fill:none}
  .guide-dash{stroke:var(--dim);stroke-width:1.2;fill:none;stroke-dasharray:5 4}
  .pack-text{font-family:"Poppins",sans-serif}
  .bold{font-weight:700}
  .semi{font-weight:600}
  .flavour-red{--flavour:var(--brand-red)}
  .flavour-hot{--flavour:var(--hot)}
  .flavour-tomyum{--flavour:var(--tomyum)}
  .flavour-pizza{--flavour:var(--pizza)}
  .flavour-bbq{--flavour:var(--bbq)}
  .flavour-fill{fill:var(--flavour)}
  .rule{stroke:var(--ink);fill:none}
</style>
</head>
<body>
<svg class="sheet" viewBox="0 0 1800 2000" xmlns="http://www.w3.org/2000/svg">
  <defs>
    <linearGradient id="artTone" x1="0" y1="1" x2="1" y2="0">
      <stop offset="0" stop-color="#b51a1a"/>
      <stop offset="1" stop-color="#d0332a"/>
    </linearGradient>

    <g id="pouch-guides">
      <rect class="guide" x="205" y="175" width="661" height="903"/>
      <line class="guide-dash" x1="230" y1="175" x2="230" y2="1078"/>
      <line class="guide-dash" x1="842" y1="175" x2="842" y2="1078"/>
      <line class="guide-dash" x1="205" y1="262" x2="866" y2="262"/>
      <line class="guide-dash" x1="205" y1="287" x2="866" y2="287"/>
      <line class="guide-dash" x1="205" y1="307" x2="866" y2="307"/>
      <path d="M205 230 l6 -4 v8z M866 230 l-6 -4 v8z" fill="var(--dim)"/>
    </g>

    <g id="thumb-front">
      <rect width="224" height="306" fill="var(--ink)"/>
      <rect x="30" y="140" width="166" height="138" rx="10" fill="var(--window)"/>
      <rect class="flavour-fill" x="70" y="0" width="84" height="17"/>
      <path d="M70 17 H154 V147 a10 10 0 0 1 -10 10 H80 a10 10 0 0 1 -10 -10Z" fill="var(--paper)"/>
      <circle cx="112" cy="82" r="21" fill="var(--brand-red)"/>
      <text class="pack-text bold" x="112" y="118" font-size="11" text-anchor="middle" fill="var(--brand-red)">Ruby Crunch</text>
      <text class="pack-text bold" x="112" y="139" font-size="6.5" text-anchor="middle" fill="var(--brand-red)">rubycrunch.com</text>
      <path class="flavour-fill" d="M0 193 H80 a10 10 0 0 1 10 10 V232 a10 10 0 0 1 -10 10 H0Z"/>
      <circle cx="0" cy="217" r="18" fill="none" stroke="#fff" stroke-opacity=".3" stroke-width="3"/>
      <line x1="30" y1="212" x2="72" y2="212" stroke="#fff" stroke-width="1.5"/>
      <text class="pack-text" x="30" y="225" font-size="6.5" fill="#fff">Sesame</text>
      <text class="pack-text" x="30" y="233" font-size="6.5" fill="#fff">Special</text>
      <rect x="62" y="228" width="36" height="18" rx="9" fill="var(--paper)"/>
      <text class="pack-text bold" x="80" y="241" font-size="10" text-anchor="middle" fill="var(--ink)">500g</text>
    </g>

    <g id="thumb-back">
      <rect width="224" height="306" fill="var(--ink)"/>
      <rect x="16" y="50" width="90" height="168" rx="8" fill="var(--paper)"/>
      <rect x="119" y="50" width="81" height="240" rx="8" fill="var(--window)"/>
      <circle cx="61" cy="80" r="18" fill="var(--brand-red)"/>
      <g stroke="var(--ink)" stroke-width=".8">
        <line x1="22" y1="116" x2="100" y2="116" stroke-width="1.6"/>
        <line x1="22" y1="124" x2="100" y2="124"/>
        <line x1="22" y1="134" x2="100" y2="134" stroke-width="1.4"/>
        <line x1="22" y1="142" x2="100" y2="142"/>
        <line x1="22" y1="148" x2="100" y2="148"/>
        <line x1="22" y1="154" x2="100" y2="154"/>
        <line x1="22" y1="160" x2="100" y2="160"/>
        <line x1="22" y1="170" x2="100" y2="170" stroke-width="1.4"/>
        <line x1="22" y1="176" x2="100" y2="176"/>
        <line x1="22" y1="182" x2="100" y2="182"/>
        <line x1="22" y1="194" x2="90" y2="194" stroke="#888"/>
        <line x1="22" y1="200" x2="96" y2="200" stroke="#888"/>
        <line x1="22" y1="206" x2="70" y2="206" stroke="#888"/>
      </g>
      <rect class="flavour-fill" x="16" y="222" width="90" height="17" rx="8"/>
      <text class="pack-text bold" x="61" y="231" font-size="5.5" text-anchor="middle" fill="#fff">PRODUCT OF SYDNEY</text>
      <text class="pack-text" x="61" y="237" font-size="3.8" text-anchor="middle" fill="#fff">Store In Cool &amp; Dry Place</text>
      <rect x="16" y="243" width="90" height="24" rx="8" fill="var(--paper)"/>
      <rect class="flavour-fill" x="16" y="272" width="90" height="18" rx="8"/>
      <circle cx="28" cy="281" r="4" fill="none" stroke="#fff" stroke-width="1"/>
      <text class="pack-text bold" x="36" y="284" font-size="7" fill="#fff">rubycrunch.com</text>
    </g>
  </defs>

  <!-- FRONT FACE -->
  <g class="pouch-front">
    <rect x="170" y="140" width="730" height="972" fill="var(--paper)" stroke="var(--ink)" stroke-width="1.5"/>
    <rect x="180" y="148" width="712" height="956" fill="var(--ink)"/>
    <use href="#pouch-guides"/>

    <rect class="clear-window" x="292" y="588" width="486" height="405" rx="25" fill="var(--window)"/>

    <g class="hang-tag">
      <rect x="413" y="148" width="245" height="79" fill="var(--brand-red)"/>
      <path d="M413 227 H658 V603 a30 30 0 0 1 -30 30 H443 a30 30 0 0 1 -30 -30Z" fill="var(--paper)"/>
      <circle cx="535" cy="420" r="58" fill="var(--brand-red)"/>
      <text class="pack-text bold" x="535" y="520" font-size="32" text-anchor="middle" fill="var(--brand-red)">Ruby Crunch</text>
      <text class="pack-text bold" x="535" y="584" font-size="19" text-anchor="middle" fill="var(--brand-red)">rubycrunch.com</text>
    </g>

    <g class="flavour-band">
      <path d="M180 746 H437 a30 30 0 0 1 30 30 V856 a30 30 0 0 1 -30 30 H180Z" fill="var(--brand-red)"/>
      <g fill="none" stroke="#fff" stroke-opacity=".25" stroke-width="6">
        <circle cx="200" cy="816" r="22"/>
        <circle cx="200" cy="816" r="44"/>
        <circle cx="200" cy="816" r="66"/>
      </g>
      <text class="pack-text bold" x="292" y="790" font-size="31" fill="#fff">ORIGINAL</text>
      <line x1="292" y1="810" x2="413" y2="810" stroke="#fff" stroke-width="4"/>
      <text class="pack-text" x="294" y="836" font-size="19" fill="#fff">Sesame</text>
      <text class="pack-text" x="294" y="856" font-size="19" fill="#fff">Special</text>
      <rect x="382" y="850" width="102" height="49" rx="24" fill="var(--paper)"/>
      <text class="pack-text bold" x="433" y="884" font-size="28" text-anchor="middle" fill="var(--ink)">500<tspan font-size="17">g</tspan></text>
    </g>

    <rect class="flavour-art" role="img" aria-label="Red chilli pepper illustration" x="500" y="728" width="278" height="262" rx="18" fill="url(#artTone)"/>

    <path class="guide-dash" d="M205 887 Q535 1210 866 887"/>
  </g>

  <!-- BACK FACE -->
  <g class="pouch-back">
    <rect x="926" y="140" width="730" height="972" fill="var(--paper)" stroke="var(--ink)" stroke-width="1.5"/>
    <rect x="934" y="148" width="714" height="956" fill="var(--ink)"/>
    <use href="#pouch-guides" transform="translate(755 0)"/>

    <rect class="clear-window" x="1310" y="326" width="238" height="702" rx="25" fill="var(--window)"/>

    <g class="nutrition-card pack-text" fill="var(--ink)">
      <rect x="1010" y="326" width="261" height="492" rx="25" fill="var(--paper)"/>
      <circle cx="1140" cy="405" r="46" fill="var(--brand-red)"/>
      <text class="bold" x="1140" y="482" font-size="22" text-anchor="middle" fill="var(--brand-red)">Ruby Crunch</text>

      <text class="semi" x="1025" y="512" font-size="14">Nutrition Information</text>
      <text class="semi" x="1025" y="524" font-size="10.5">Serving Per Package</text>
      <text class="semi" x="1253" y="524" font-size="10.5" text-anchor="end">10</text>
      <line class="rule" x1="1024" y1="529" x2="1256" y2="529" stroke-width="4"/>
      <text x="1025" y="545" font-size="10.5">Serving Size</text>
      <text x="1253" y="545" font-size="10.5" text-anchor="end">100g</text>
      <line class="rule" x1="1024" y1="554" x2="1256" y2="554" stroke-width="1"/>
      <text class="semi" x="1025" y="576" font-size="10.5">Average Quantity</text>
      <text class="semi" x="1128" y="576" font-size="10.5">Per Serving</text>
      <text class="semi" x="1197" y="576" font-size="10.5">Per 100mg</text>
      <line class="rule" x1="1024" y1="583" x2="1256" y2="583" stroke-width="3"/>

      <g font-size="10.5">
        <text x="1025" y="601">Energy</text><text x="1175" y="601" text-anchor="end">2367kj</text><text x="1253" y="601" text-anchor="end">2367kj</text>
        <line class="rule" x1="1024" y1="605" x2="1256" y2="605"/>
        <text x="1025" y="618">Protein</text><text x="1171" y="618" text-anchor="end">8.8g</text><text x="1253" y="618" text-anchor="end">8.8g</text>
        <line class="rule" x1="1024" y1="622" x2="1256" y2="622"/>
        <text x="1025" y="635">Fat</text><text x="1173" y="635" text-anchor="end">37.2g</text><text x="1253" y="635" text-anchor="end">37.2g</text>
        <line class="rule" x1="1024" y1="639" x2="1256" y2="639"/>
        <text x="1025" y="651">Carbohydrate</text><text x="1173" y="651" text-anchor="end">49.5g</text><text x="1253" y="651" text-anchor="end">49.5g</text>
        <line class="rule" x1="1024" y1="655" x2="1256" y2="655"/>
        <text x="1025" y="667">Sodium</text><text x="1180" y="667" text-anchor="end">6767mg</text><text x="1253" y="667" text-anchor="end">6767mg</text>
      </g>
      <line class="rule" x1="1024" y1="689" x2="1256" y2="689" stroke-width="2"/>
      <g font-size="10.5">
        <text x="1025" y="705">*Vitamin</text><text x="1128" y="705" text-anchor="end">A 0%</text><text x="1150" y="705">*Vitamin C</text><text x="1253" y="705" text-anchor="end">2%</text>
        <line class="rule" x1="1024" y1="710" x2="1256" y2="710"/>
        <text x="1025" y="722">*Calcium</text><text x="1128" y="722" text-anchor="end">10%</text><text x="1150" y="722">*Iron</text><text x="1253" y="722" text-anchor="end">10%</text>
        <line class="rule" x1="1024" y1="727" x2="1256" y2="727"/>
        <text x="1025" y="739">*Vitamin</text><text x="1128" y="739" text-anchor="end">B12</text><text x="1150" y="739">*0% Magnisium</text><text x="1253" y="739" text-anchor="end">12%</text>
      </g>
      <line class="rule" x1="1024" y1="744" x2="1256" y2="744" stroke-width="2"/>
      <g font-size="8.5">
        <text x="1025" y="765">#All values are averages</text>
        <text x="1025" y="779">Crunchy Chilli Snack: Original Sesame</text>
        <text x="1025" y="789">Ingredients: Dried red chilli 97% White sesame seeds</text>
        <text x="1025" y="799">2% Crispy flour 1%</text>
      </g>
    </g>

    <g class="origin-pill pack-text">
      <rect x="1010" y="828" width="261" height="49" rx="24" fill="var(--brand-red)"/>
      <text class="bold" x="1140" y="851" font-size="18" text-anchor="middle" fill="#fff">PRODUCT OF SYDNEY</text>
      <text x="1140" y="868" font-size="13" text-anchor="middle" fill="#fff">Store In Cool &amp; Dry Place</text>
    </g>
    <rect class="code-panel" x="1010" y="886" width="261" height="80" rx="24" fill="var(--paper)"/>
    <g class="web-pill pack-text">
      <rect x="1010" y="978" width="261" height="50" rx="25" fill="var(--brand-red)"/>
      <g fill="none" stroke="#fff" stroke-width="1.6">
        <circle cx="1056" cy="1003" r="12"/>
        <ellipse cx="1056" cy="1003" rx="5" ry="12"/>
        <line x1="1044" y1="1003" x2="1068" y2="1003"/>
      </g>
      <text class="bold" x="1078" y="1010" font-size="19" fill="#fff">rubycrunch.com</text>
    </g>
  </g>

  <!-- DIMENSIONS -->
  <g class="dimensions">
    <g class="width-front">
      <text class="dim-text" x="218" y="72" font-size="19" text-anchor="middle">7mm</text>
      <text class="dim-text" x="218" y="90" font-size="19" text-anchor="middle">Seal</text>
      <text class="dim-text" x="854" y="72" font-size="19" text-anchor="middle">7mm</text>
      <text class="dim-text" x="854" y="90" font-size="19" text-anchor="middle">Seal</text>
      <text class="dim-text" x="536" y="90" font-size="30" text-anchor="middle">Total Width_190mm</text>
      <text class="dim-text" x="536" y="127" font-size="27" text-anchor="middle">176mm</text>
      <path class="dim-line" d="M205 100 H866 M205 130 H866 M205 92 V138 M230 120 V138 M842 120 V138 M866 92 V138"/>
    </g>
    <g class="width-back">
      <text class="dim-text" x="973" y="72" font-size="19" text-anchor="middle">7mm</text>
      <text class="dim-text" x="973" y="90" font-size="19" text-anchor="middle">Seal</text>
      <text class="dim-text" x="1609" y="72" font-size="19" text-anchor="middle">7mm</text>
      <text class="dim-text" x="1609" y="90" font-size="19" text-anchor="middle">Seal</text>
      <text class="dim-text" x="1291" y="90" font-size="30" text-anchor="middle">Total Width_190mm</text>
      <text class="dim-text" x="1291" y="127" font-size="27" text-anchor="middle">176mm</text>
      <path class="dim-line" d="M960 100 H1621 M960 130 H1621 M960 92 V138 M985 120 V138 M1597 120 V138 M1621 92 V138"/>
    </g>
    <g class="height-left">
      <text class="dim-text" x="72" y="226" font-size="19" text-anchor="middle">Cut</text>
      <text class="dim-text" x="72" y="244" font-size="19" text-anchor="middle">Mark</text>
      <path class="dim-line" d="M92 230 H170 M100 175 V1078 M92 175 H170 M92 1078 H170 M120 175 V230 M165 175 V1078 M140 262 H170 M140 307 H170 M112 887 V1078 M100 887 H140"/>
      <text class="dim-text" font-size="38" text-anchor="middle" transform="translate(92 626) rotate(-90)">Total Height_260mm</text>
      <text class="dim-text" font-size="18" text-anchor="middle" transform="translate(133 198) rotate(-90)">15mm</text>
      <text class="dim-text" font-size="24" text-anchor="middle" transform="translate(161 220) rotate(-90)">25mm</text>
      <text class="dim-text" font-size="16" text-anchor="middle" transform="translate(139 285) rotate(-90)">13mm</text>
      <text class="dim-text" font-size="16" text-anchor="middle" transform="translate(157 285) rotate(-90)">Zipper</text>
      <text class="dim-text" font-size="24" text-anchor="middle" transform="translate(161 693) rotate(-90)">222mm</text>
      <text class="dim-text" font-size="28" text-anchor="middle" transform="translate(137 982) rotate(-90)">55mm Gusset</text>
    </g>
    <g class="height-right">
      <path class="dim-line" d="M1660 175 V1078 M1652 175 H1668 M1652 262 H1668 M1652 307 H1668 M1652 1078 H1668 M1690 887 V1078 M1682 887 H1698 M1682 1078 H1698"/>
      <text class="dim-text" font-size="24" text-anchor="middle" transform="translate(1664 220) rotate(90)">25mm</text>
      <text class="dim-text" x="1662" y="291" font-size="18">13mm Zipper</text>
      <text class="dim-text" font-size="24" text-anchor="middle" transform="translate(1664 693) rotate(90)">222mm</text>
      <text class="dim-text" font-size="28" text-anchor="middle" transform="translate(1664 985) rotate(90)">55mm Gusset</text>
    </g>
  </g>

  <!-- FLAVOUR RANGE – FRONTS -->
  <g class="range-fronts pack-text">
    <g class="flavour-red" transform="translate(442 1200)">
      <use href="#thumb-front"/>
      <text class="bold" x="30" y="208" font-size="11" fill="#fff">ORIGINAL</text>
      <rect role="img" aria-label="Red chilli pepper illustration" x="128" y="188" width="66" height="88" rx="8" fill="#c8201f"/>
    </g>
    <g class="flavour-hot" transform="translate(690 1200)">
      <use href="#thumb-front"/>
      <text class="bold" x="30" y="208" font-size="9" fill="#fff">HOT &amp; SPICY</text>
      <rect role="img" aria-label="Flaming hot chilli illustration" x="138" y="212" width="56" height="64" rx="8" fill="#d8321c"/>
    </g>
    <g class="flavour-tomyum" transform="translate(937 1200)">
      <use href="#thumb-front"/>
      <text class="bold" x="30" y="208" font-size="10" fill="#fff">TOM YUM</text>
      <rect role="img" aria-label="Tom yum soup bowl illustration" x="122" y="218" width="72" height="58" rx="8" fill="#e27a3a"/>
    </g>
    <g class="flavour-pizza" transform="translate(1185 1200)">
      <use href="#thumb-front"/>
      <text class="bold" x="30" y="208" font-size="10" fill="#fff">PIZZA</text>
      <rect role="img" aria-label="Pizza slice illustration" x="118" y="216" width="76" height="60" rx="8" fill="#f2b53a"/>
    </g>
    <g class="flavour-bbq" transform="translate(1432 1200)">
      <use href="#thumb-front"/>
      <text class="bold" x="30" y="208" font-size="10" fill="#fff">BBQ</text>
      <rect role="img" aria-label="Barbecue grill with flames illustration" x="122" y="218" width="72" height="58" rx="8" fill="#c8201f"/>
    </g>
  </g>

  <!-- FLAVOUR RANGE – BACKS -->
  <g class="range-backs">
    <use class="flavour-red" href="#thumb-back" transform="translate(442 1540)"/>
    <use class="flavour-hot" href="#thumb-back" transform="translate(690 1540)"/>
    <use class="flavour-tomyum" href="#thumb-back" transform="translate(937 1540)"/>
    <use class="flavour-pizza" href="#thumb-back" transform="translate(1185 1540)"/>
    <use class="flavour-bbq" href="#thumb-back" transform="translate(1432 1540)"/>
  </g>
</svg>
</body>
</html>
```